KLB Wealth - Business card Miles Dorsett

On Front of card:
Logo, Name, Title, phone, email,
website: TheDorsettCircle.com and CA Insurance license
For phone number we want a phone Icon or a "P" or "T"

On back of card:
The Dorsett Circle LLC
(555) 318-2094
Address
QR code, if it fits
Disclosure at bottom of card.(See attachment)

Logo Colors:

Blue:
HEX: #0f75bc
RGB: rgba(15,117,188,255)
Grey:
HEX: #6d6e71
RGB: rgba(109,110,113,255

Industry/Entity Type

wealth Management, Personal Finance

Contact Information for Business Card

On Front of card: Logo, Name, Title, phone, email, website: TheDorsettCircle.com and CA Insurance license For phone number we want a phone Icon or a "P" or "T" On back of card: The Dorsett Circle LLC Address QR code, if it fits Disclosure at bottom of card.(See attachment) Logo Colors: Blue: HEX: #0f75bc RGB: rgba(15,117,188,255) Grey: HEX: #6d6e71 RGB: rgba(109,110,113,255

Requirements
Must have
• be horizontal and no gimmicks (see through)
Nice to have
• Prefer clean and crisp
Should not have
• No black for background, no letterpress and angled view

```html
<!DOCTYPE html>
<html lang="en">
<head>
<meta charset="utf-8">
<title>KLB Wealth – Business Card – Miles Dorsett</title>
<link rel="stylesheet" href="https://fonts.googleapis.com/css2?family=Libre+Baskerville:wght@700&family=Montserrat:wght@400;500&display=swap">
<style>
  :root {
    --backdrop: #cfd3d4;
    --paper: #f7f8f8;
    --brand-blue: #0f4f9e;
    --accent-blue: #0f75bc;
    --ink: #3a3b3e;
    --brand-grey: #6d6e71;
    --watermark: #e3ebf2;
  }
  * { box-sizing: border-box; margin: 0; padding: 0; }
  html, body { width: 1200px; height: 829px; overflow: hidden; }
  body {
    background: var(--backdrop);
    display: flex;
    align-items: center;
    justify-content: center;
    gap: 48px;
    font-family: "Montserrat", Arial, sans-serif;
  }
  .card {
    position: relative;
    width: 525px;
    height: 300px;
    background: var(--paper);
    border-bottom: 4px solid var(--accent-blue);
    box-shadow: 0 10px 26px rgba(0,0,0,0.18);
    overflow: hidden;
  }
  .wordmark {
    font-family: "Libre Baskerville", Georgia, serif;
    font-weight: 700;
    color: var(--brand-blue);
    white-space: nowrap;
  }

  /* Front */
  .card-front .wordmark {
    position: absolute;
    left: 34px;
    top: 34px;
    font-size: 34px;
  }
  .contact {
    position: absolute;
    left: 34px;
    top: 142px;
    list-style: none;
    font-size: 13px;
    line-height: 25px;
    color: var(--ink);
  }
  .contact .label { color: var(--accent-blue); margin-right: 4px; }
  .contact .license { font-size: 11px; color: var(--brand-grey); }
  .identity {
    position: absolute;
    right: 34px;
    top: 138px;
    text-align: right;
  }
  .identity .name {
    font-family: "Libre Baskerville", Georgia, serif;
    font-weight: 700;
    font-size: 16px;
    letter-spacing: 0.5px;
    color: var(--brand-blue);
    text-transform: uppercase;
  }
  .identity .title {
    font-size: 13px;
    color: var(--ink);
    margin-top: 3px;
  }
  .monogram {
    position: absolute;
    right: 36px;
    bottom: 16px;
    font-family: "Libre Baskerville", Georgia, serif;
    font-weight: 700;
    font-size: 86px;
    color: var(--watermark);
    line-height: 1;
  }

  /* Back */
  .card-back {
    display: flex;
    flex-direction: column;
    align-items: center;
    padding: 34px 30px 18px;
    text-align: center;
  }
  .card-back .wordmark { font-size: 40px; }
  .company {
    margin-top: 22px;
    font-size: 14px;
    font-weight: 500;
    color: var(--brand-blue);
  }
  .company-details {
    margin-top: 6px;
    font-size: 12px;
    line-height: 20px;
    color: var(--ink);
  }
  .company-details .label { color: var(--accent-blue); margin-right: 4px; }
  .disclosure {
    margin-top: auto;
    font-size: 8px;
    line-height: 11px;
    color: var(--brand-grey);
    max-width: 460px;
  }
</style>
</head>
<body>
  <section class="card card-front" aria-label="Card front">
    <div class="wordmark">KLB Wealth</div>
    <ul class="contact">
      <li><span class="label">P:</span>555-318-2094</li>
      <li>MilesD@TheDorsettCircle.com</li>
      <li>TheDorsettCircle.com</li>
      <li class="license">CA Insurance Lic. #0K48213</li>
    </ul>
    <div class="identity">
      <div class="name">Miles Dorsett</div>
      <div class="title">Wealth Advisor</div>
    </div>
    <div class="monogram" aria-hidden="true">KLB</div>
  </section>

  <section class="card card-back" aria-label="Card back">
    <div class="wordmark">KLB Wealth</div>
    <div class="company">The Dorsett Circle LLC</div>
    <div class="company-details">
      <div><span class="label">P:</span>(555) 318-2094</div>
      <div>2270 Larkfield Avenue, Suite 140, Fairmont, CA 90000</div>
    </div>
    <p class="disclosure">Advisory services are offered through The Dorsett Circle LLC. Investing involves risk, including possible loss of principal. Insurance products are offered through licensed agents.</p>
  </section>
</body>
</html>
```